Business card design needed

We are a company that provides women with executive support. We organise a range of services including - transportation, relocation, home and office support and bespoke custom fit garments and anything to assist in their busy lifestyle.

The colours we would like are bright blue on the back and front is white with design. We have an example card that we would be happy to use. My son designed these cards but did not print well. Happy for you to use his design by tweaking it and adding a description of our service on the back of the card and making the back look easier to read . Also need the hotmail address and phone and abn. We will also need a website organised through pluma - are you able to add www.brightlaneassist.com.au to the card..?. Any questions pls contact me on 0417586293 Mara

Thank you
Updates

business card needed to start new business - please note sample of business card we are happy for you to use.

Industry/Entity Type

Business

Contact Information for Business Card

The brightlane crew
Let us organise you!

Executive support for women

brightlanecrew@maildrop-example.com
ph: Mara 0417 586 293 or Joan 0438 270 915
abn: 21604873519

```html
<!DOCTYPE html>
<html lang="en">
<head>
<meta charset="utf-8">
<title>The brightlane crew – Business Cards</title>
<link rel="stylesheet" href="https://fonts.googleapis.com/css2?family=Arimo:wght@400;700&display=swap">
<style>
  :root {
    --backdrop: #e6e6e8;
    --card-front: #f4f4f4;
    --card-back: #1c78e0;
    --ink: #3b3b3e;
    --ink-light: #ffffff;
    --ink-soft: #dcebff;
    --accent: #d6232a;
    --shadow: rgba(0, 0, 0, 0.18);
  }
  * { box-sizing: border-box; margin: 0; padding: 0; }
  html, body {
    width: 1200px;
    height: 900px;
    overflow: hidden;
    background: var(--backdrop);
    font-family: "Arimo", Arial, sans-serif;
    color: var(--ink);
  }
  .sheet {
    width: 1200px;
    height: 900px;
    display: flex;
    flex-direction: column;
    align-items: center;
    justify-content: center;
    gap: 44px;
  }
  .card {
    position: relative;
    width: 640px;
    height: 380px;
    box-shadow: 0 10px 28px var(--shadow);
    overflow: hidden;
  }

  /* Brand lockup: invented name + one plain mark */
  .brand {
    position: absolute;
    display: flex;
  }
  .brand-mark {
    flex: none;
    border-radius: 50%;
  }
  .brand-name {
    font-weight: 700;
    text-transform: uppercase;
    line-height: 1;
    letter-spacing: 0.02em;
  }

  /* Back: bright blue contact side */
  .card--back {
    background: var(--card-back);
    color: var(--ink-light);
  }
  .card--back .brand {
    left: 40px;
    top: 38px;
    align-items: center;
    gap: 14px;
  }
  .card--back .brand-mark { width: 28px; height: 28px; background: var(--ink-light); }
  .card--back .brand-name { font-size: 26px; color: var(--ink-light); }
  .service-line {
    position: absolute;
    left: 40px;
    top: 116px;
    font-size: 19px;
    font-weight: 700;
    color: var(--ink-light);
  }
  .service-description {
    position: absolute;
    left: 40px;
    top: 148px;
    width: 250px;
    font-size: 14px;
    line-height: 1.45;
    color: var(--ink-soft);
  }
  .holder-name {
    position: absolute;
    left: 40px;
    bottom: 38px;
    font-size: 22px;
    letter-spacing: 0.04em;
    text-transform: uppercase;
  }
  .contact-list {
    position: absolute;
    left: 320px;
    bottom: 38px;
    list-style: none;
    font-size: 14.5px;
    line-height: 1.5;
  }
  .contact-list .label { color: var(--ink-soft); }

  /* Front: white logo side */
  .card--front { background: var(--card-front); }
  .card--front .brand {
    left: 78px;
    top: 92px;
    align-items: flex-end;
    gap: 22px;
  }
  .card--front .brand-mark { width: 80px; height: 80px; background: var(--accent); margin-bottom: 4px; }
  .card--front .brand-text { display: flex; flex-direction: column; }
  .card--front .brand-name { font-size: 56px; color: var(--ink); }
  .brand-last-line { display: flex; align-items: baseline; gap: 16px; }
  .tagline {
    font-size: 21px;
    color: var(--accent);
    white-space: nowrap;
  }
</style>
</head>
<body>
  <main class="sheet">
    <section class="card card--back" aria-label="Business card, contact side">
      <div class="brand">
        <span class="brand-mark" aria-hidden="true"></span>
        <span class="brand-name">The brightlane<br>crew</span>
      </div>
      <p class="service-line">Executive Support For Women</p>
      <p class="service-description">Transportation, relocation, home and office support, bespoke custom fit garments and more for your busy lifestyle.</p>
      <p class="holder-name">Mara Ellison</p>
      <ul class="contact-list">
        <li><span class="label">ph:</span> Mara 0417 586 293</li>
        <li><span class="label">ph:</span> Joan 0438 270 915</li>
        <li>brightlanecrew@maildrop-example.com</li>
        <li>www.brightlaneassist.com.au</li>
        <li><span class="label">abn:</span> 21604873519</li>
      </ul>
    </section>

    <section class="card card--front" aria-label="Business card, logo side">
      <div class="brand">
        <span class="brand-mark" aria-hidden="true"></span>
        <div class="brand-text">
          <span class="brand-name">The</span>
          <span class="brand-name">brightlane</span>
          <div class="brand-last-line">
            <span class="brand-name">crew</span>
            <span class="tagline">Let Us Organise You!</span>
          </div>
        </div>
      </div>
    </section>
  </main>
</body>
</html>
```